依頼詳細
主にポスティング用です。

保存率が高くなるようなデザインをお願いします。(用紙サイズは問いません)

地元である事をアピールしたいです。

当社は静岡市上下水道指定工事店 焼津市上下水道指定工事店 藤枝市上水道指定工事店です。

現在使用している水漏れ等のチラシを添付します。
スタッフ写真も添付しますが使わなくてもかまいません。

住所を 静岡市メインのものと焼津市、藤枝市メインのもの二つ欲しいです。(納品時で結構です)

記載項目
有限会社 浜風工業
本社 焼津市柳原3丁目8-24  054-391-2584
静岡営業所 静岡市葵区川辺新町9-3  054-437-1928
フリーダイヤル 0120-569-382
サイズ
A4以下
ページ数
片面
希望イメージ
シンプル 複雑
単色 カラフル
暗い 明るい
日常 高級
遊び心 厳粛
未来的 伝統的
女性的 男性的
希望する色
お任せします
納品ファイル
• 高解像度JPG (.jpg)
• イラストレーター形式 (.ai)
• PNG形式 (.png)
補足説明
■ 選んだ理由

文字の目立たせ方、色目、キャラクター等気に入りました。清潔感がありながら一番目立たせたい文字もしっかり目立っていて良かったです。

■ 提案者全員のお礼・コメント

ご提案して下さった皆様本当にありがとうございました。
当選決定まで時間がかかってしましすみません。迷いました。
内容の良いものも多かったのですが見た目のイメージの良かったものを選ばせて頂きました。
機会がありましたらまた宜しくお願い致します。

```html
<!DOCTYPE html>
<html lang="ja">
<head>
<meta charset="utf-8">
<title>浜風工業 水漏れ・つまり修理</title>
<link rel="stylesheet" href="https://fonts.googleapis.com/css2?family=M+PLUS+Rounded+1c:wght@800;900&family=Noto+Sans+JP:wght@400;700;900&display=swap">
<style>
  :root{
    --orange:#f39800;
    --orange-deep:#e97b00;
    --red:#e60012;
    --blue:#0068b7;
    --navy:#1d2f7a;
    --yellow:#fff100;
    --white:#ffffff;
    --cream:#fff6e0;
    --ink:#222222;
  }
  *{box-sizing:border-box;margin:0;padding:0}
  html,body{width:848px;height:1200px;overflow:hidden}
  body{font-family:"Noto Sans JP",sans-serif;background:var(--white);color:var(--ink)}
  .flyer{position:relative;width:848px;height:1200px;background:var(--orange);overflow:hidden}

  .headline{position:absolute;left:18px;top:14px;font-family:"M PLUS Rounded 1c",sans-serif;font-weight:900;color:var(--red);line-height:1.02;font-size:112px;letter-spacing:-2px;-webkit-text-stroke:12px var(--white);paint-order:stroke fill}
  .certified{position:absolute;left:408px;top:14px;width:424px;height:82px;background:var(--white);border:5px solid var(--yellow);border-radius:8px;color:var(--blue);font-weight:900;font-size:25px;line-height:1.25;text-align:center;padding-top:6px}

  .services{position:absolute;left:402px;top:104px;width:430px;height:214px;background:var(--blue);border-radius:12px;padding:10px}
  .services__inner{background:var(--white);border-radius:8px;height:136px;padding:6px 14px;color:var(--red);font-weight:900;font-size:40px;line-height:1.04}
  .services__action{color:var(--white);font-weight:900;font-size:52px;text-align:center;line-height:60px;margin-top:2px}
  .small-jobs{position:absolute;right:8px;top:86px;width:96px;height:96px;border-radius:50%;background:var(--yellow);border:3px solid var(--white);color:var(--navy);font-weight:700;font-size:15px;line-height:1.3;display:flex;align-items:center;justify-content:center;text-align:center}

  .prices{position:absolute;left:18px;top:254px;width:372px;background:var(--blue);border-radius:10px;padding:8px}
  .prices__row{display:flex;justify-content:space-between;background:var(--white);color:var(--red);font-weight:900;font-size:25px;line-height:36px;padding:0 10px;border-radius:4px}
  .prices__row+.prices__row{margin-top:5px}

  .local{position:absolute;left:14px;top:384px;width:560px;font-weight:900;color:var(--navy);font-size:37px;line-height:1.3;-webkit-text-stroke:8px var(--white);paint-order:stroke fill}
  .local .accent{color:var(--red)}

  .staff{position:absolute;left:582px;top:336px;width:250px;height:188px;border-radius:8px;background:linear-gradient(180deg,#c9d6e4,#8a9db3);border:4px solid var(--white)}
  .staff__note{position:absolute;left:582px;top:336px;width:118px;background:var(--white);color:var(--red);font-size:13px;font-weight:700;line-height:1.35;padding:6px;border-radius:0 0 8px 0}

  .promise{position:absolute;left:18px;top:540px;width:556px;height:96px;background:var(--white);border-radius:8px;padding:8px 12px;font-size:13px;line-height:1.55}
  .promise__title{display:inline-block;background:var(--red);color:var(--white);font-weight:900;font-size:15px;padding:0 10px;border-radius:10px;margin-bottom:2px}

  .works{position:absolute;left:18px;top:648px;width:812px;display:grid;grid-template-columns:repeat(4,1fr);grid-auto-rows:128px;gap:10px}
  .work{background:var(--white);border-radius:10px;padding:6px;display:flex;flex-direction:column}
  .work__art{flex:1;border-radius:6px;background:linear-gradient(180deg,#e3eef8,#b9cfe4)}
  .work__label{color:var(--red);font-weight:900;font-size:14px;line-height:1.25;text-align:center;margin-top:4px}

  .contact{position:absolute;left:0;top:1062px;width:848px;height:100px;background:var(--white);display:flex;align-items:center;padding:0 18px;gap:12px}
  .contact__lead{width:100px;color:var(--navy);font-weight:700;font-size:13px;line-height:1.35}
  .contact__dial{display:flex;align-items:center;gap:8px;color:var(--blue);font-weight:900;font-size:70px;letter-spacing:-1px;line-height:1}
  .contact__company{margin-left:auto;color:var(--navy);font-weight:900;font-size:30px;line-height:1.1;text-align:right}
  .contact__company small{display:block;font-size:16px}
  .offices{position:absolute;left:0;top:1162px;width:848px;height:38px;background:var(--navy);color:var(--white);font-size:15px;font-weight:700;display:flex;align-items:center;justify-content:center;gap:24px}
</style>
</head>
<body>
<main class="flyer">
  <h1 class="headline">水漏れ<br>つまり</h1>

  <div class="certified">焼津市上下水道指定工事店<br>藤枝市上下水道指定工事店</div>

  <section class="services">
    <div class="services__inner">ガス給湯器<br>電気温水器<br>ボイラー</div>
    <div class="services__action">修理/交換</div>
    <div class="small-jobs">小さなお仕事も<br>お気軽に</div>
  </section>

  <section class="prices">
    <p class="prices__row"><span>蛇口の水漏れ修理</span><span>¥3,000～</span></p>
    <p class="prices__row"><span>トイレのつまり</span><span>¥5,000～</span></p>
    <p class="prices__row"><span>配水管のつまり</span><span>¥3,000～</span></p>
  </section>

  <p class="local">焼津・藤枝<span class="accent">市内すぐに伺います!</span><br>地元業者だから安心!<br>全て自社施行だから<span class="accent">低料金!</span></p>

  <div class="staff" role="img" aria-label="作業着姿のスタッフ集合写真"></div>
  <p class="staff__note">市内全域うかがいます。お気軽にご連絡ください!</p>

  <section class="promise">
    <span class="promise__title">安心の約束</span>
    <p>● 見積り・お見積もり料は無料です。作業前に必ず料金をご説明します。</p>
    <p>● 追加料金は事前にご相談し、ご了承なく作業を進めることはありません。</p>
    <p>● 施工後もしっかりアフターフォロー。気になる点はいつでもご連絡を。</p>
  </section>

  <section class="works">
    <div class="work"><div class="work__art" role="img" aria-label="トイレタンクのイラスト"></div><p class="work__label">トイレの水漏れ修理<br>タンク内修理</p></div>
    <div class="work"><div class="work__art" role="img" aria-label="給水管のイラスト"></div><p class="work__label">給水管・排水管<br>修理</p></div>
    <div class="work"><div class="work__art" role="img" aria-label="蛇口とシャワーのイラスト"></div><p class="work__label">蛇口・シャワーの取替え<br>水漏れ修理</p></div>
    <div class="work"><div class="work__art" role="img" aria-label="井戸ポンプのイラスト"></div><p class="work__label">井戸のポンプ修理<br>取り替え</p></div>
    <div class="work"><div class="work__art" role="img" aria-label="排水管のイラスト"></div><p class="work__label">配水管のつまり</p></div>
    <div class="work"><div class="work__art" role="img" aria-label="台所と洗面所のイラスト"></div><p class="work__label">台所・洗面所<br>水漏れ修理</p></div>
    <div class="work"><div class="work__art" role="img" aria-label="床下配管のイラスト"></div><p class="work__label">床下漏水</p></div>
    <div class="work"><div class="work__art" role="img" aria-label="混合水栓のイラスト"></div><p class="work__label">混合水栓<br>修理・交換</p></div>
    <div class="work"><div class="work__art" role="img" aria-label="洋式トイレのイラスト"></div><p class="work__label">トイレのリフォーム<br>洋式トイレ交換</p></div>
    <div class="work"><div class="work__art" role="img" aria-label="水回り部品のイラスト"></div><p class="work__label">部品・補修<br>水回り全般</p></div>
    <div class="work"><div class="work__art" role="img" aria-label="浄化槽のイラスト"></div><p class="work__label">浄化槽・下水<br>接続工事</p></div>
    <div class="work"><div class="work__art" role="img" aria-label="公共下水道のイラスト"></div><p class="work__label">公共下水道<br>接続工事</p></div>
  </section>

  <section class="contact">
    <p class="contact__lead">お申し込み・<br>お問い合わせは<br>こちら</p>
    <p class="contact__dial">
      <svg width="56" height="56" viewBox="0 0 24 24" aria-hidden="true"><path fill="currentColor" d="M6.6 10.8a15.1 15.1 0 0 0 6.6 6.6l2.2-2.2c.3-.3.7-.4 1-.2 1.1.4 2.3.6 3.6.6.6 0 1 .4 1 1V20c0 .6-.4 1-1 1A17 17 0 0 1 3 4c0-.6.4-1 1-1h3.5c.6 0 1 .4 1 1 0 1.3.2 2.5.6 3.6.1.3 0 .7-.2 1z"/></svg>
      0120-569-382
    </p>
    <p class="contact__company"><small>有限会社</small>浜風工業</p>
  </section>

  <footer class="offices">
    <span>本社：焼津市柳原3丁目8-24　TEL.054-391-2584</span>
    <span>静岡営業所：静岡市葵区川辺新町9-3　TEL.054-437-1928</span>
  </footer>
</main>
</body>
</html>
```